Business card design needed for Automotive Reconditioning business

I have a logo design i just cant decide on the best color or layout for the business card, I will upload all the files so you can see all colors schemes we are considering. I have other file formats if needed let me know.

Target Market(s)

automotive dealerships

Contact Information for Business Card

HERE are the Descriptions and info needed on the card:
Interior Repair: Leather carpet burns panels dash Deoderize
Dealer products and Vin Verify
( spot for name and cell number) My name is Dorian Pelk phone 951 430-2158 Title COO www.BrolvexMotor.com

Font styles to use
Sans Serif
Other font styles liked:
• what ever you think looks best

Requirements
Must have
• Must be able to change the name and phone for employees

```html
<!DOCTYPE html>
<html lang="en">
<head>
<meta charset="utf-8">
<title>Brolvex Motor Reconditioning Corp. — Business Card</title>
<link rel="stylesheet" href="https://fonts.googleapis.com/css2?family=Roboto:wght@400;500;700;900&display=swap">
<style>
  :root {
    --stage: #b4b4b4;
    --brand-blue: #284c88;
    --ink-blue: #23488a;
    --text-grey: #444a52;
    --rule-blue: #3d5d99;
    --card-white: #ffffff;
  }
  * { margin: 0; padding: 0; box-sizing: border-box; }
  html, body {
    width: 1200px;
    height: 930px;
    overflow: hidden;
  }
  body {
    background: var(--stage);
    font-family: "Roboto", Arial, sans-serif;
    position: relative;
  }
  .card {
    position: absolute;
    left: 290px;
    width: 620px;
    height: 354px;
    border-radius: 26px;
    box-shadow: 0 8px 20px rgba(0,0,0,0.18);
    overflow: hidden;
  }
  .card--back {
    top: 64px;
    background: var(--brand-blue);
    display: flex;
    align-items: center;
    justify-content: center;
  }
  .card--front {
    top: 502px;
    background: var(--card-white);
  }
  .wordmark {
    font-weight: 900;
    text-transform: uppercase;
    text-align: center;
    line-height: 1.05;
    letter-spacing: 0.5px;
  }
  .wordmark__main { display: block; font-size: 42px; }
  .wordmark__sub { display: block; font-size: 17px; letter-spacing: 1.5px; margin-top: 6px; }
  .card--back .wordmark { color: var(--card-white); }
  .card--front .wordmark {
    color: var(--brand-blue);
    position: absolute;
    left: 36px;
    top: 178px;
    width: 300px;
  }
  .card--front .wordmark__main { font-size: 35px; }
  .card--front .wordmark__sub { font-size: 14px; }
  .divider {
    position: absolute;
    left: 358px;
    top: 60px;
    width: 2px;
    height: 222px;
    background: var(--rule-blue);
  }
  .contact {
    position: absolute;
    left: 382px;
    top: 52px;
    color: var(--text-grey);
    font-size: 15px;
  }
  .contact__name {
    color: var(--ink-blue);
    font-size: 28px;
    font-weight: 400;
    letter-spacing: 1px;
    text-transform: uppercase;
  }
  .contact__title { font-size: 15px; margin: 2px 0 12px 8px; letter-spacing: 1px; }
  .contact__address { line-height: 1.45; margin-left: 22px; margin-bottom: 8px; }
  .contact__list { list-style: none; margin-left: 30px; }
  .contact__list li {
    display: flex;
    align-items: center;
    gap: 9px;
    line-height: 1.5;
  }
  .contact__icon { width: 12px; height: 12px; flex: none; }
  .contact__web strong { color: var(--ink-blue); font-weight: 500; }
</style>
</head>
<body>

  <section class="card card--back" aria-label="Card back">
    <p class="wordmark">
      <span class="wordmark__main">Brolvex Motor</span>
      <span class="wordmark__sub">Reconditioning Corp.</span>
    </p>
  </section>

  <section class="card card--front" aria-label="Card front">
    <p class="wordmark">
      <span class="wordmark__main">Brolvex Motor</span>
      <span class="wordmark__sub">Reconditioning Corp.</span>
    </p>

    <div class="divider"></div>

    <div class="contact">
      <h1 class="contact__name">Dorian Pelk</h1>
      <p class="contact__title">COO</p>
      <p class="contact__address">214b Harlow Street,<br>Ashbury, NZ, 8042</p>
      <ul class="contact__list">
        <li>
          <svg class="contact__icon" viewBox="0 0 12 12" aria-hidden="true"><path d="M3 1 L5 3.5 L4 5 Q5.5 7 7 8 L8.5 7 L11 9 L9.5 11 Q5 11 1 3 Z" fill="#23488a"/></svg>
          <span>951 430-2158</span>
        </li>
        <li>
          <svg class="contact__icon" viewBox="0 0 12 12" aria-hidden="true"><rect x="1" y="2.5" width="10" height="7" fill="none" stroke="#23488a" stroke-width="1.2"/><path d="M1 2.5 L6 6.5 L11 2.5" fill="none" stroke="#23488a" stroke-width="1.2"/></svg>
          <span>info@brolvexmotor.com</span>
        </li>
        <li class="contact__web">
          <svg class="contact__icon" viewBox="0 0 12 12" aria-hidden="true"><circle cx="6" cy="6" r="5" fill="none" stroke="#23488a" stroke-width="1.1"/><ellipse cx="6" cy="6" rx="2.2" ry="5" fill="none" stroke="#23488a" stroke-width="0.9"/><path d="M1 6 H11" stroke="#23488a" stroke-width="0.9"/></svg>
          <span>www.<strong>brolvexmotor</strong>.com</span>
        </li>
      </ul>
    </div>
  </section>

</body>
</html>
```